Prairie 2014 District Meeting

This flyer will be printed on a 4" x 6" flyer.

Requirements
Must have
• Flyer must be done in landscape format

Please use only 1 of the 3 uploaded skyline photos as a background

Zeta Kappa Chapter, Sigma Rho Tau Fraternity, Inc. Proudly Hosts the 64th Annual 5th District Meeting In Oklahoma City

April 17th - 20th 2014

Host Hotel: Halvorne, Oklahoma City (405) 555-0147

District Marshall: Bro. Curtis Fenley (405) 555-0193
Deputy District Marshall: Bro. Leon Pratt
Nice to have
• Purple & Gold are the fraternity's colors

```html
<!DOCTYPE html>
<html lang="en">
<head>
<meta charset="utf-8">
<title>Prairie 2014 District Meeting</title>
<link rel="stylesheet" href="https://fonts.googleapis.com/css2?family=Bebas+Neue&family=Questrial&family=Petit+Formal+Script&display=swap">
<style>
  :root {
    --page: #ffffff;
    --ink-dark: #0b0309;
    --purple-deep: #2a0a26;
    --purple-glow: #b21fa3;
    --purple-mid: #5c1856;
    --gold-light: #fbe9a6;
    --gold: #e2b84a;
    --gold-dark: #a97a1c;
    --white: #ffffff;
    --frame: rgba(190, 180, 195, 0.55);
  }
  * { margin: 0; padding: 0; box-sizing: border-box; }
  html, body {
    width: 1200px; height: 1000px; overflow: hidden;
    background: var(--page);
  }
  .flyer {
    position: absolute; left: 96px; top: 165px;
    width: 1008px; height: 672px;
    overflow: hidden; background: var(--ink-dark);
    color: var(--white);
  }
  .skyline { position: absolute; inset: 0; width: 100%; height: 100%; }
  .host {
    position: absolute; left: 42px; top: 38px;
  }
  .host-name {
    font-family: "Bebas Neue", sans-serif;
    font-size: 23px; letter-spacing: 0.3px; line-height: 1;
  }
  .host-line {
    font-family: "Questrial", sans-serif;
    font-size: 17px; margin-top: 6px; letter-spacing: 0.4px;
  }
  .emblem-name {
    position: absolute; left: 0; width: 100%; top: 150px;
    text-align: center;
    font-family: "Bebas Neue", sans-serif;
    font-size: 34px; letter-spacing: 2px; color: var(--gold);
  }
  .frame {
    position: absolute; left: 61px; top: 228px;
    width: 888px; height: 407px;
    border: 6px solid var(--frame);
    background: rgba(10, 2, 10, 0.35);
  }
  .content {
    position: absolute; left: 0; top: 268px; width: 100%;
    text-align: center;
  }
  .gold {
    background: linear-gradient(180deg, var(--gold-light) 0%, var(--gold) 50%, var(--gold-dark) 100%);
    -webkit-background-clip: text; background-clip: text;
    color: transparent;
  }
  .title {
    font-family: "Bebas Neue", sans-serif;
    font-size: 60px; line-height: 1; letter-spacing: 0.5px;
  }
  .city {
    font-family: "Petit Formal Script", cursive;
    font-size: 40px; margin-top: 8px; line-height: 1.1;
  }
  .dates {
    font-family: "Bebas Neue", sans-serif;
    font-size: 34px; margin-top: 38px; line-height: 1;
  }
  .divider {
    width: 338px; height: 2px; margin: 8px auto 10px;
    background: var(--white);
  }
  .venue {
    font-family: "Bebas Neue", sans-serif;
    font-size: 30px; line-height: 1.2;
  }
  .officers {
    font-family: "Questrial", sans-serif;
    font-size: 17px; line-height: 1.35; margin-top: 42px;
  }
  .officers strong { font-weight: 700; }
</style>
</head>
<body>
  <main class="flyer">
    <svg class="skyline" role="img" aria-label="Night aerial photo of the Oklahoma City skyline glowing in purple light" viewBox="0 0 1008 672" preserveAspectRatio="none">
      <defs>
        <linearGradient id="sky" x1="0" y1="0" x2="0" y2="1">
          <stop offset="0" stop-color="#060105"/>
          <stop offset="0.27" stop-color="#1c0619"/>
          <stop offset="0.31" stop-color="#9a1c8c"/>
          <stop offset="0.36" stop-color="#5c1856"/>
          <stop offset="0.6" stop-color="#2a0a26"/>
          <stop offset="0.85" stop-color="#3a0f35"/>
          <stop offset="1" stop-color="#0d030c"/>
        </linearGradient>
        <radialGradient id="glow" cx="0.5" cy="0.6" r="0.6">
          <stop offset="0" stop-color="#b21fa3" stop-opacity="0.35"/>
          <stop offset="1" stop-color="#b21fa3" stop-opacity="0"/>
        </radialGradient>
      </defs>
      <rect width="1008" height="672" fill="url(#sky)"/>
      <rect width="1008" height="672" fill="url(#glow)"/>
    </svg>

    <header class="host">
      <p class="host-name">Zeta Kappa Chapter, Sigma Rho Tau Fraternity, Inc.</p>
      <p class="host-line">proudly hosts</p>
    </header>

    <p class="emblem-name">Sigma Rho Tau</p>

    <div class="frame"></div>

    <section class="content">
      <h1 class="title gold">The 64th Annual 5th District Meeting</h1>
      <p class="city">in Oklahoma City</p>
      <p class="dates gold">April 17th -20th, 2014</p>
      <div class="divider"></div>
      <p class="venue">Halvorne Hotel, Oklahoma City</p>
      <p class="venue">(405) 555-0147</p>
      <div class="officers">
        <p><strong>District Marshall:</strong> Bro. Curtis Fenley (405) 555-0193</p>
        <p><strong>Deputy District Marshall:</strong> Bro. Leon Pratt</p>
      </div>
    </section>
  </main>
</body>
</html>
```